Lorena Vex Wigs " Styling Foam"

I need a label created for my product . The bottle size is 50ml so it must be designed to fit that size bottle. I will post my logo and examples of my bottle size. I want the label design to be simple and cute. ill also add pictures of my website, so you can get ideas from there. The bottle is white so I want the main colors to be white and pink. All colors on the label must match my logo. I love glitter as well.

I know for sure I want my logo big, and I want "Styling Foam'',
then under styling foam I would like " Medium Hold" in a different front. be very creative.

Then under that I would like it to say " No Alcohol , Saulfate or Paraben

please make sure on the label in the front it has "NET: 7.0 oz / 200g" so people know what size it is.

I would like a glitter border on the label.

I also want the back of the label to have directions.

And ingredients list too . Very small not too big at all.

Target Market(s)

My target market is woman of all ages .. but mainly woman from ages 26-65

Industry/Entity Type

Hair And Beauty

Font styles to use
Serif
Sans Serif
Decorative
Script

Colors
e667a6
eda3c7
f9d9e8
e34297

Requirements
Must have
• The project must match the colors of my logo, it must have a nice pretty glitter border . It must be simple and clean . But still stylish ! I don’t want everything after my logo to be in the same font . Have fun with this design, be creative. My logo and “ Styling Foam” must be the two centerpiece!
Nice to have
• It will be nice to have different fonts! And nice to have all the colors that match my logo
Must be expensive looking !!
Very eye catching!
Should not have
• Do not add colors that my logo doesn’t have !!!!
I don’t want it to look too plain and boring ! I want it to be classy and expensive looking !

```html
<!DOCTYPE html>
<html lang="en">
<head>
<meta charset="utf-8">
<title>Lorena Vex Wigs – Styling Foam Label</title>
<link rel="stylesheet" href="https://fonts.googleapis.com/css2?family=Montserrat:wght@300;400;500&family=Cormorant+Garamond:wght@500&display=swap">
<style>
  :root {
    --backdrop: #f9d9e8;
    --label-white: #ffffff;
    --brand-pink: #e34297;
    --soft-pink: #e667a6;
    --text-grey: #8a8a8e;
    --silver-light: #d9d9dc;
    --silver-dark: #9a9aa0;
  }
  html, body {
    margin: 0;
    padding: 0;
    width: 1150px;
    height: 1200px;
    overflow: hidden;
    background: var(--backdrop);
  }
  .label {
    position: absolute;
    left: 215px;
    top: 60px;
    width: 720px;
    height: 1080px;
    background: var(--label-white);
    border-radius: 6px;
    overflow: hidden;
    text-align: center;
    font-family: "Montserrat", sans-serif;
  }
  .brand-name {
    position: absolute;
    top: 140px;
    left: 0;
    width: 100%;
    margin: 0;
    font-family: "Montserrat", sans-serif;
    font-weight: 500;
    font-size: 64px;
    letter-spacing: 3px;
    line-height: 1.15;
    color: var(--brand-pink);
  }
  .product-name {
    position: absolute;
    top: 430px;
    left: 0;
    width: 100%;
    margin: 0;
    font-weight: 400;
    font-size: 50px;
    letter-spacing: 2px;
    color: var(--brand-pink);
  }
  .hold-strength {
    position: absolute;
    top: 508px;
    left: 0;
    width: 100%;
    margin: 0;
    font-family: "Cormorant Garamond", serif;
    font-weight: 500;
    font-size: 26px;
    letter-spacing: 3px;
    color: var(--text-grey);
  }
  .free-from {
    position: absolute;
    top: 600px;
    left: 0;
    width: 100%;
    margin: 0;
    font-weight: 300;
    font-size: 22px;
    line-height: 1.4;
    color: var(--text-grey);
  }
  .glitter-band {
    position: absolute;
    left: 0;
    top: 720px;
    width: 720px;
    height: 180px;
  }
  .net-weight {
    position: absolute;
    top: 980px;
    left: 0;
    width: 100%;
    margin: 0;
    font-weight: 400;
    font-size: 20px;
    letter-spacing: 1px;
    color: var(--text-grey);
  }
</style>
</head>
<body>
  <main class="label">
    <h1 class="brand-name">Lorena Vex<br>Wigs</h1>
    <h2 class="product-name">STYLING FOAM</h2>
    <p class="hold-strength">~ MEDIUM HOLD ~</p>
    <p class="free-from">No Alcohol<br>Saulfate or Paraben</p>
    <svg class="glitter-band" viewBox="0 0 720 180" role="img" aria-label="Silver glitter wave border">
      <defs>
        <linearGradient id="silver-glitter" x1="0" y1="0" x2="1" y2="1">
          <stop offset="0" stop-color="var(--silver-light)"/>
          <stop offset="0.5" stop-color="var(--silver-dark)"/>
          <stop offset="1" stop-color="var(--silver-light)"/>
        </linearGradient>
      </defs>
      <path d="M0 150 C 200 150, 420 120, 720 40 L 720 85 C 460 150, 220 175, 0 178 Z" fill="url(#silver-glitter)"/>
    </svg>
    <p class="net-weight">NET: 7.0 oz / 200g</p>
  </main>
</body>
</html>
```